Gleeful Minnie’s Crunch

I am looking for a new peanut brittle design for my packaging/business. I want a design that speaks of that “homemade” brittle you had as a child. Colors that are warm, but not too dark. Please note*** "Gleeful Minnie's Crunch (with a Capital "B"). The logo attached does not have the "B" capitalized and they left out the Gleeful in the title. Again, looking for warm colors- think early fall colors and peanuts! LOL. Please see my uploads and I've attached a package design (this is from a stock photo which the previous designer DID NOT create on his own) And it doesn't have the Gleeful Minnie's Crunch either. But you get the idea. Looking forward to seeing the designs.

Thank you for reading this! :-)

```html
<!DOCTYPE html>
<html lang="en">
<head>
<meta charset="utf-8">
<title>Gleeful Minnie’s Crunch – Classic Peanut Brittle Pouch</title>
<link href="https://fonts.googleapis.com/css2?family=Fraunces:opsz,wght@9..144,800&family=Montserrat:wght@600;700&display=swap" rel="stylesheet">
<style>
  :root {
    --backdrop: #ff7250;
    --cream: #f3e5bf;
    --cream-shade: #ecd8ab;
    --maroon: #8c2545;
    --rose: #9b4560;
    --coral: #f0735a;
  }
  * { margin: 0; padding: 0; box-sizing: border-box; }
  html, body { width: 1200px; height: 960px; overflow: hidden; background: var(--backdrop); }
  .canvas { position: relative; width: 1200px; height: 960px; background: var(--backdrop); }
  .pouch { position: absolute; left: 344px; top: 136px; width: 489px; height: 684px; }
  .pouch-art { position: absolute; inset: 0; width: 489px; height: 684px; display: block; }
  .brand-name {
    position: absolute; left: 0; right: 0; top: 176px;
    text-align: center;
    font-family: "Fraunces", Georgia, serif;
    font-weight: 800; font-size: 60px; line-height: 66px;
    color: var(--rose);
  }
  .tagline {
    position: absolute; left: 0; right: 0; top: 392px;
    text-align: center;
    font-family: "Montserrat", Arial, sans-serif;
    font-weight: 600; font-size: 12px; letter-spacing: 2.4px;
    color: var(--maroon);
  }
  .flavor {
    position: absolute; left: 82px; width: 331px; top: 471px; height: 26px;
    display: flex; align-items: center; justify-content: center;
    font-family: "Montserrat", Arial, sans-serif;
    font-weight: 700; font-size: 19px; letter-spacing: 0.3px;
    color: var(--cream);
  }
  .net-weight {
    position: absolute; left: 0; right: 0; top: 543px;
    text-align: center;
    font-family: "Montserrat", Arial, sans-serif;
    font-weight: 700; font-size: 17px;
    color: var(--maroon);
  }
</style>
</head>
<body>
<main class="canvas">
  <section class="pouch">
    <svg class="pouch-art" viewBox="0 0 489 684" aria-hidden="true">
      <defs>
        <clipPath id="pouch-shape">
          <path d="M12,0 H477 Q489,0 489,12 V684 H0 V12 Q0,0 12,0 Z"/>
        </clipPath>
        <radialGradient id="brittle-tone" cx="50%" cy="40%" r="70%">
          <stop offset="0" stop-color="#f3e5bf"/>
          <stop offset="1" stop-color="#efdcb0"/>
        </radialGradient>
      </defs>
      <g clip-path="url(#pouch-shape)">
        <rect class="stripe-base" x="0" y="470" width="489" height="214" fill="var(--cream)"/>
        <g class="stripes" fill="var(--coral)">
          <rect x="30" y="470" width="40" height="214"/>
          <rect x="108" y="470" width="40" height="214"/>
          <rect x="186" y="470" width="40" height="214"/>
          <rect x="264" y="470" width="40" height="214"/>
          <rect x="342" y="470" width="40" height="214"/>
          <rect x="420" y="470" width="40" height="214"/>
        </g>
        <path class="upper-panel" d="M0,0 H489 V505 Q244,680 0,505 Z" fill="url(#brittle-tone)"/>
        <path class="curve-band" d="M0,505 Q244,680 489,505" fill="none" stroke="var(--maroon)" stroke-width="14"/>
      </g>
      <rect role="img" aria-label="Faint pattern of hand-drawn peanut brittle pieces scattered across the pouch" x="0" y="0" width="489" height="1" fill="none"/>
      <circle class="tear-notch" cx="0" cy="73" r="6" fill="var(--backdrop)"/>
      <circle class="tear-notch" cx="489" cy="73" r="6" fill="var(--backdrop)"/>
      <path class="flavor-ribbon" d="M82,471 H413 L406,483.5 L413,496 H82 L89,483.5 Z" fill="var(--maroon)"/>
    </svg>
    <h1 class="brand-name">Gleeful<br>Minnie’s<br>Crunch</h1>
    <p class="tagline">MADE FRESH ONE BAG AT A TIME</p>
    <p class="flavor">CLASSIC PEANUT BRITTLE</p>
    <p class="net-weight">NET: 5oz (142g)</p>
  </section>
</main>
</body>
</html>
```